Smart Proposal Template

I would like to create a reusable proposal template to be used for selling business to business products or services. Please see the attached word doc. The template must have expandable/contractable fields allowing the user to populate it with data without disrupting the format.. Please see the attached sample. The red font represents sample data for guiding the user in how to complete the template. This data must be able to be removed when the user ads in their actual data.

Target Market(s)

business owners

Font styles to use
Sans Serif

Colors
ec1f27
ffffff

Requirements
Must have
• template must be a tool that allows the users to fill in the blanks.
the red font that i have is text for suggesting how the users fill in the field.
The header must allow the user to replace my title with theirs.

```html
<!DOCTYPE html>
<html lang="en">
<head>
<meta charset="utf-8">
<title>Contents</title>
<link rel="stylesheet" href="https://fonts.googleapis.com/css2?family=Open+Sans:wght@400;600;800&display=swap">
<style>
  :root {
    --backdrop: #bb8a82;
    --paper: #ffffff;
    --brand-red: #ec1f27;
    --ink: #1e1e1e;
    --ink-soft: #3c3c3c;
    --muted: #9a9a9a;
    --accent-dark: #3a3a3a;
  }
  * { box-sizing: border-box; margin: 0; padding: 0; }
  html, body {
    width: 1200px;
    height: 900px;
    overflow: hidden;
  }
  body {
    background: var(--backdrop);
    font-family: "Open Sans", Arial, sans-serif;
    position: relative;
  }
  .page {
    position: absolute;
    left: 296px;
    top: 20px;
    width: 608px;
    height: 860px;
    background: var(--paper);
    box-shadow: 0 10px 30px rgba(0,0,0,0.22);
    overflow: hidden;
  }
  .contents-header {
    position: absolute;
    left: 62px;
    top: 92px;
    width: 440px;
    height: 44px;
  }
  .contents-header__bar {
    position: absolute;
    left: 10px;
    top: 0;
    width: 430px;
    height: 14px;
    background: var(--brand-red);
    z-index: 0;
  }
  .contents-header__marker {
    position: absolute;
    left: 0;
    top: 10px;
    width: 6px;
    height: 22px;
    background: var(--accent-dark);
  }
  .contents-header__title {
    position: absolute;
    left: 14px;
    top: 4px;
    z-index: 1;
    font-weight: 800;
    font-size: 25px;
    line-height: 1;
    color: var(--ink);
    letter-spacing: 0.5px;
    text-transform: uppercase;
  }
  .toc {
    position: absolute;
    left: 66px;
    top: 186px;
    right: 30px;
    list-style: none;
  }
  .toc__item {
    display: flex;
    align-items: baseline;
    margin-bottom: 25px;
    font-size: 10.5px;
    text-transform: uppercase;
    color: var(--ink-soft);
    letter-spacing: 0.3px;
    white-space: nowrap;
  }
  .toc__number {
    flex: 0 0 42px;
    color: var(--muted);
    font-size: 10px;
  }
  .page-footer {
    position: absolute;
    right: 18px;
    bottom: 36px;
    font-size: 8px;
    color: var(--muted);
    letter-spacing: 0.3px;
  }
  .page-footer__band {
    position: absolute;
    right: 0;
    bottom: 0;
    width: 62%;
    height: 22px;
    background: var(--brand-red);
  }
</style>
</head>
<body>
  <main class="page">
    <header class="contents-header">
      <span class="contents-header__bar"></span>
      <span class="contents-header__marker"></span>
      <h1 class="contents-header__title">Contents</h1>
    </header>

    <ol class="toc">
      <li class="toc__item"><span class="toc__number">01</span><span class="toc__title">Introduction</span></li>
      <li class="toc__item"><span class="toc__number">02</span><span class="toc__title">Your Business Objectives</span></li>
      <li class="toc__item"><span class="toc__number">03</span><span class="toc__title">Alternate Strategies Considered</span></li>
      <li class="toc__item"><span class="toc__number">04</span><span class="toc__title">We Anticipate the Following Schedule for the Delivering Our Solution</span></li>
      <li class="toc__item"><span class="toc__number">05</span><span class="toc__title">Uniquely Qualified</span></li>
      <li class="toc__item"><span class="toc__number">06</span><span class="toc__title">Corporate Overview</span></li>
    </ol>

    <p class="page-footer">Proposal Document | 02</p>
    <div class="page-footer__band"></div>
  </main>
</body>
</html>
```